Poster for Kirtan Music Event

Design (3) 24" x 36" Posters

I have provided a sample a friend did in Australia: ( Picture No. 4 )

Use all the text on sample poster except the replacement changes below.

Replace with the following text as this is for different location:
Replacement Text:

Every Friday Night 7:00pm-8:30pm
Halewai Stretch & Rhythm Loft
742 Mellory St Kealu

Free Kirtan Experience! or Free Event
Rohan Velu & Companions

Optional Text:

A evening of music, singing of spiritual mantras, and refreshments

Bring flowers, musical instruments, friends, or just come with an open heart.

Meditate on transcendental sounds that provide rest for the mind & heart"

An evening of music & singing of sacred mantra's

```html
<!DOCTYPE html>
<html lang="en">
<head>
<meta charset="utf-8">
<title>Free Kirtan Experience Poster</title>
<link href="https://fonts.googleapis.com/css2?family=Exo+2:wght@500;600;700;800&display=swap" rel="stylesheet">
<style>
  :root {
    --page-bg: #e9e4dc;
    --sun-white: #fffbe0;
    --sun-yellow: #ffe23a;
    --gold: #f2c20f;
    --deep-gold: #e0a50a;
    --maroon: #4a0a0a;
    --maroon-shadow: #8a3a12;
    --rust: #7a3d0c;
    --text-brown: #8c4a12;
    --title-yellow: #fff200;
    --body-yellow: #ffe94a;
  }
  * { margin: 0; padding: 0; box-sizing: border-box; }
  html, body { width: 1200px; height: 1000px; overflow: hidden; }
  body {
    background: var(--page-bg);
    font-family: "Exo 2", "Trebuchet MS", sans-serif;
    position: relative;
  }
  .poster {
    position: absolute;
    left: 300px; top: 50px;
    width: 600px; height: 900px;
    overflow: hidden;
    background:
      radial-gradient(circle at 30% 8%, var(--sun-white) 0%, var(--sun-yellow) 22%, var(--gold) 55%, var(--deep-gold) 100%);
    box-shadow: 0 6px 24px rgba(0,0,0,0.25);
  }
  .performers-photo {
    position: absolute;
    left: 110px; top: 70px;
    width: 490px; height: 400px;
    background:
      radial-gradient(ellipse at 62% 45%, rgba(40,30,40,0.55) 0%, rgba(120,80,60,0.35) 35%, rgba(242,194,15,0) 70%),
      radial-gradient(ellipse at 35% 70%, rgba(235,225,210,0.75) 0%, rgba(210,150,110,0.45) 35%, rgba(242,194,15,0) 70%);
  }
  .shapes { position: absolute; inset: 0; }
  .line {
    position: absolute;
    left: 0; width: 600px;
    text-align: center;
    white-space: nowrap;
    line-height: 1;
  }
  .event-title {
    top: 491px;
    font-size: 35px; font-weight: 800;
    color: var(--title-yellow);
    transform: rotate(-6.3deg);
    letter-spacing: -0.3px;
  }
  .host-name {
    top: 540px; left: -4px;
    font-size: 30px; font-weight: 700;
    color: var(--maroon);
    transform: rotate(-4deg);
  }
  .details {
    font-size: 22px; font-weight: 500;
    color: var(--text-brown);
    transform: rotate(-4deg);
  }
  .details.time { top: 592px; left: 4px; }
  .details.venue { top: 618px; left: 8px; }
  .details.address { top: 644px; left: 10px; }
  .invite {
    position: absolute;
    left: 75px; width: 480px;
    text-align: center;
    font-size: 16px; font-weight: 500;
    line-height: 20px;
    color: var(--body-yellow);
    transform: rotate(-4deg);
  }
  .invite.one { top: 723px; }
  .invite.two { top: 777px; }
  .invite.three { top: 822px; }
</style>
</head>
<body>
  <main class="poster">
    <div class="performers-photo" role="img" aria-label="Photo of two kirtan musicians, one singing with a guitar and one playing a hand drum, glowing in warm sunlight"></div>

    <svg class="shapes" width="600" height="900" viewBox="0 0 600 900" aria-hidden="true">
      <polygon class="title-band-shadow" points="66,490 545,438 548,510 66,560" fill="var(--maroon-shadow)"/>
      <polygon class="title-band" points="58,484 537,431 540,502 58,552" fill="var(--maroon)"/>
      <polygon class="info-box" points="77,712 549,654 549,900 70,900" fill="var(--maroon)"/>
      <polygon class="info-box-strip" points="70,875 549,843 549,900 70,900" fill="var(--rust)"/>
    </svg>

    <h1 class="line event-title">FREE KIRTAN EXPERIENCE!</h1>
    <h2 class="line host-name">Rohan Velu &amp; Companions</h2>
    <p class="line details time">Every Friday Night 7:00pm-8:30pm</p>
    <p class="line details venue">Halewai Stretch &amp; Rhythm Loft</p>
    <p class="line details address">742 Mellory St Kealu</p>

    <p class="invite one">A evening of music, mantra, refreshments and<br>spiritual discourse.</p>
    <p class="invite two">Bring flowers, musical instruments, friends, or<br>just come with an open heart.</p>
    <p class="invite three">An evening of music &amp; singing of sacred mantra's</p>
  </main>
</body>
</html>
```